hfdhddfgfhfghfghgfhfhfhgfhfhfh

Industry/Entity Type

Painting

Logo Text

TOLVEN Painting

Logo styles of interest
Wordmark Logo
Requirements
Should not have
• Paintbrushes or rollers etc....

```html
<!DOCTYPE html>
<html lang="en">
<head>
<meta charset="utf-8">
<title>Tolven Painting – Business Card</title>
<link rel="stylesheet" href="https://fonts.googleapis.com/css2?family=Arimo:ital,wght@0,400;0,700;1,400&family=Roboto+Slab:wght@700&display=swap">
<style>
  :root {
    --page: #ffffff;
    --card-blue: #1f5ea8;
    --card-blue-deep: #184f93;
    --brand-red: #d23a2c;
    --brand-cream: #f6ead0;
    --name-gold: #f2cf6f;
    --text-white: #ffffff;
    --banner-tan: #cfae72;
    --banner-ink: #3a2a14;
  }
  * { margin: 0; padding: 0; box-sizing: border-box; }
  html, body {
    width: 900px; height: 1200px; overflow: hidden;
    background: var(--page);
  }
  .sheet { position: relative; width: 900px; height: 1200px; }
  .card {
    position: absolute; left: 0; width: 900px;
    background: radial-gradient(ellipse at 40% 40%, var(--card-blue) 0%, var(--card-blue-deep) 100%);
    overflow: hidden;
  }
  .card--front { top: 15px; height: 570px; }
  .card--back { top: 630px; height: 555px; }

  .brand { position: absolute; display: flex; align-items: center; gap: 14px; }
  .brand__dot { border-radius: 50%; background: var(--brand-red); flex: none; }
  .brand__name {
    font-family: "Arimo", sans-serif; font-weight: 700;
    letter-spacing: 1px; color: var(--brand-cream); white-space: nowrap;
  }
  .card--front .brand { left: 72px; top: 155px; }
  .card--front .brand__dot { width: 80px; height: 80px; }
  .card--front .brand__name { font-size: 34px; }

  .card--back .brand { left: 50%; top: 150px; transform: translateX(-50%); }
  .card--back .brand__dot { width: 64px; height: 64px; }
  .card--back .brand__name { font-size: 28px; }

  .contact {
    position: absolute; right: 45px; top: 320px;
    text-align: right; font-family: "Arimo", sans-serif;
    color: var(--text-white); font-size: 29px; line-height: 40px;
  }
  .contact__name { font-weight: 700; color: var(--name-gold); }
  .contact__line { font-style: italic; }

  .banner {
    position: absolute; left: 205px; top: 290px; width: 610px; height: 110px;
    background: var(--banner-tan); border-radius: 6px;
    transform: rotate(-4deg);
    display: flex; align-items: center; justify-content: center;
  }
  .banner__text {
    font-family: "Roboto Slab", serif; font-weight: 700;
    font-size: 28px; color: var(--banner-ink); white-space: nowrap;
  }
</style>
</head>
<body>
<main class="sheet">
  <section class="card card--front">
    <div class="brand">
      <span class="brand__dot"></span>
      <span class="brand__name">TOLVEN PAINTING</span>
    </div>
    <div class="contact">
      <p class="contact__name">Lukas Tolven</p>
      <p class="contact__line">Managing Director.</p>
      <p class="contact__line">ABN-Number 41 597 203 816.</p>
      <p class="contact__line">mobile number 0487 315 960</p>
      <p class="contact__line">tolvenpainting@mailbox.com</p>
    </div>
  </section>

  <section class="card card--back">
    <div class="brand">
      <span class="brand__dot"></span>
      <span class="brand__name">TOLVEN PAINTING</span>
    </div>
    <div class="banner" role="img" aria-label="Decorative tan ribbon banner carrying the service line">
      <span class="banner__text">Domestic, Residential &amp; Commercial</span>
    </div>
  </section>
</main>
</body>
</html>
```